WP website design for Brevin

We need a wordpress design for an auction company. The winning design will incorporate a professional color scheme with company logo in a clean, image driven layout. The design needs to consider that this will be developed on a responsive theme. Colors are those that will highlight the logo.

Industry/Entity Type

It Company

Font styles to use
Serif
Sans Serif

Colors

Designer to choose colors to be used in the design.

Requirements
Must have
• Navigation: 1) Home 2) Auctions 3) Services 4) Real Estate 5 ) Previous Auctions 6) About Us 7) Contact Us

Sites referenced that client likes: https://www.pledgora.example/ and http://www.quillmoorbids.example/ as examples of image rich sites. There will be large slideshow element and 4 calls to action (with any stock images suitable) 1) Real Estate 2) Auctions 3) Liquidations 4) Appraisals

Content will also include text (below) and auctions as seen at http://www.quillmoorbids.example/ below the slideshow or as in the attached image.

Footer will have contact info, social icons (FB, Microblog, YT, RSS) and news posts widget

Colors will be that of the logo and any others to highlight/compliment the design.

Nice to have
• Use of dropdown menu styling

```html
<!DOCTYPE html>
<html lang="en">
<head>
<meta charset="utf-8">
<title>Brevin Auctions</title>
<link href="https://fonts.googleapis.com/css2?family=Open+Sans:wght@300;400;600;700&display=swap" rel="stylesheet">
<style>
:root{
  --navy:#1b2d72;
  --navy-deep:#0e1d55;
  --navy-light:#2d4496;
  --ink:#2a2a2a;
  --text:#4a4a4a;
  --muted:#6b6b6b;
  --page:#ececec;
  --panel:#f3f3f3;
  --line:#d9d9d9;
  --white:#ffffff;
  --cta:#1c1c1c;
}
*{box-sizing:border-box;margin:0;padding:0}
html,body{width:1200px;height:2804px;overflow:hidden}
body{font-family:"Open Sans",Arial,sans-serif;color:var(--text);background:var(--page);position:relative;font-size:12px}
.abs{position:absolute}

/* header */
.site-header{left:0;top:0;width:1200px;height:103px;background:#f4f4f4}
.brand{left:172px;top:22px;display:flex;align-items:center;gap:12px}
.brand-mark{width:22px;height:22px;background:var(--navy)}
.brand-name{font-size:30px;font-weight:700;color:var(--navy);letter-spacing:.5px}
.call{right:178px;top:42px;display:flex;align-items:center;gap:8px;font-size:21px;font-weight:700;color:var(--ink)}
.call svg{width:22px;height:22px}

/* nav */
.main-nav{left:0;top:103px;width:1200px;height:69px;background:linear-gradient(#2b3f8e,var(--navy-deep));border-bottom:2px solid #0a153f}
.main-nav ul{list-style:none;display:flex;gap:8px;position:absolute;left:182px;top:18px}
.main-nav li{color:#fff;font-size:15px;font-weight:600;padding:6px 14px;border-radius:2px}
.main-nav li.active{background:#23378a;box-shadow:inset 0 0 0 1px #3a52a8}

/* hero */
.hero{left:0;top:172px;width:1200px;height:520px;background:linear-gradient(100deg,#7d6f63 0%,#c9b9a6 35%,#e9e3dc 60%,#b8aa9d 100%)}
.hero-caption{left:172px;top:318px;width:370px;height:215px;background:rgba(20,20,25,.72);border-radius:3px;padding:26px 28px}
.hero-caption h1{font-weight:300;font-size:42px;line-height:44px;color:#fff}
.hero-caption h1 b{font-weight:700;color:#4d6bd0}
.hero-caption p{color:#ddd;font-size:11px;line-height:19px;margin-top:8px;width:280px}
.dots{display:flex;gap:6px;margin-top:16px}
.dots i{width:8px;height:8px;border-radius:50%;background:#fff;display:block}
.dots i.on{background:#4d6bd0}
.cta-row{left:172px;top:609px;display:flex;gap:13px}
.cta{width:205px;height:68px;background:linear-gradient(#3a3a3a,var(--cta));border-radius:2px;display:flex;align-items:center;gap:14px;padding-left:14px;color:#fff;font-size:14px;font-weight:600}
.cta.current{background:linear-gradient(#26398f,var(--navy-deep))}
.cta .ico{width:36px;height:36px}

/* auctions column */
.section-title{font-size:15px;font-weight:700;color:var(--ink)}
.auction{left:172px;width:563px;height:362px;background:var(--panel);border:1px solid var(--line);box-shadow:0 1px 3px rgba(0,0,0,.12);border-radius:3px}
.auction-head{height:45px;border-bottom:1px solid var(--line);padding:15px 16px;font-size:12px;font-weight:600;color:var(--ink);background:linear-gradient(#fafafa,#ececec)}
.thumb{left:13px;top:65px;width:161px;height:145px}
.tools{left:13px;top:219px;width:161px}
.tool{height:32px;margin-bottom:6px;background:linear-gradient(#fff,#dcdcdc);display:flex;align-items:center;padding-left:16px;gap:22px;font-size:13px;color:#333}
.tool svg{width:13px;height:13px}
.blurb{left:189px;top:65px;width:360px;height:112px;background:#fff;padding:10px 12px;border-radius:2px}
.blurb h3{font-size:12.5px;line-height:18px;color:var(--navy-light);font-weight:400}
.blurb p{font-size:10.5px;line-height:17px;color:#333}
.details{left:189px;top:189px;width:360px;height:153px;background:#fff;padding:10px 12px;border-radius:2px;font-size:10.5px;line-height:19px;color:#333}
.details h4{font-size:11px;font-weight:400;color:var(--navy-light);margin-bottom:2px}
.btn-bid{display:inline-flex;align-items:center;gap:8px;margin-top:8px;height:30px;width:203px;padding-left:12px;background:var(--navy);color:#fff;border-radius:4px;font-size:10.5px}
.btn-bid svg{width:14px;height:14px}

.pager{left:383px;top:2285px;display:flex;gap:10px;align-items:center}
.pager span{width:21px;height:21px;border:1px solid #ccc;background:#fff;font-size:9px;display:flex;align-items:center;justify-content:center;color:#444}
.pager span.on{background:#333;color:#fff;border-color:#333}
.pager span.gap{border:none;background:none}

/* sidebar */
.widget{left:753px;width:275px;background:var(--panel);border:1px solid var(--line);box-shadow:0 1px 3px rgba(0,0,0,.1);border-radius:3px;padding:0 13px}
.widget-title{font-size:15px;font-weight:700;color:var(--ink);padding-top:12px;display:flex;justify-content:space-between}
.arrows{font-size:13px;letter-spacing:4px}
.w-img{width:250px;height:150px;margin-top:20px}
.w-lead{font-size:11px;line-height:18px;color:var(--navy-light);font-weight:600;margin-top:10px}
.w-text{font-size:11px;line-height:19px;color:#444}
.btn-small{display:inline-block;margin-top:12px;height:30px;line-height:30px;padding:0 16px;background:var(--navy);color:#fff;font-size:11px;border-radius:3px}
.posted{font-size:11px;color:#555;margin-top:12px}
.quote-person{display:flex;align-items:center;gap:12px;margin-top:16px}
.avatar{width:103px;height:103px;border-radius:50%;background:radial-gradient(circle at 50% 40%,#cfd4da,#8a94a3)}
.quote-person b{display:block;font-size:17px;font-weight:400;color:var(--navy-light)}
.quote-person small{font-size:12px;color:#444}
.qmark{font-size:40px;line-height:30px;color:#333;font-weight:700;margin-top:6px;font-family:Georgia,serif}

/* accreditations */
.accred{left:0;top:2364px;width:1200px;height:99px;background:#e2e2e2}
.accred-label{left:199px;top:38px;font-size:15px;color:#333}
.badges{left:318px;top:22px;display:flex;gap:28px;align-items:center}
.badge{width:72px;height:52px;background:#9c9c9c;border-radius:4px}
.badge.round{border-radius:50%;width:56px}

/* footer */
.footer{left:0;top:2463px;width:1200px;height:275px;background:#f6f6f6}
.f-col{top:44px}
.f-col h5{font-size:13px;font-weight:700;color:var(--navy);margin-bottom:30px;letter-spacing:.3px}
.f-col ul{list-style:none;font-size:11.5px;line-height:21px;color:#444}
.f-col p{font-size:11.5px;line-height:19px;color:#444}
.newsitem{display:flex;gap:12px}
.date{flex:none;width:52px;height:52px;border-radius:50%;background:var(--navy);color:#fff;font-size:10px;text-align:center;padding-top:12px;line-height:14px}
.newsitem h6{font-size:11.5px;font-weight:600;color:#333;line-height:19px;margin-bottom:12px}
.social li{display:flex;justify-content:space-between;width:130px;margin-bottom:20px;align-items:center}
.social i{width:20px;height:20px;border-radius:50%;background:var(--navy);display:block}
.copyright{left:0;top:2738px;width:1200px;height:66px;background:#ececec;text-align:center;font-size:11px;color:#444;padding-top:26px}
</style>
</head>
<body>

<header class="site-header abs">
  <div class="brand abs"><span class="brand-mark"></span><span class="brand-name">BREVIN AUCTIONS</span></div>
  <div class="call abs">
    <svg viewBox="0 0 24 24"><circle cx="12" cy="12" r="12" fill="#1b2d72"/><path d="M8 6c1 0 2 2 2 3s-1 1-1 2 2 3 3 3 1-1 2-1 3 1 3 2-1 3-3 3C10 18 6 14 6 9c0-2 1-3 2-3z" fill="#fff"/></svg>
    Call Now : 1-800-555-0147
  </div>
</header>

<nav class="main-nav abs">
  <ul>
    <li class="active">HOME</li><li>AUCTIONS</li><li>SERVICES</li><li>REAL ESTATE</li><li>PREVIOUS AUCTIONS</li><li>ABOUT US</li><li>CONTACT US</li>
  </ul>
</nav>

<section class="hero abs" role="img" aria-label="Photo of a hand signing a document at a desk"></section>
<div class="hero-caption abs">
  <h1><b>Brevin</b><br>Auctions</h1>
  <p>Lorem Ipsum is simply dummy text of the printing and typesetting industry. Lorem Ipsum has been the industry's standard dummy text ever</p>
  <div class="dots"><i class="on"></i><i></i><i></i><i></i></div>
</div>

<div class="cta-row abs">
  <div class="cta"><svg class="ico" viewBox="0 0 36 36"><path d="M4 18 18 5l14 13h-4v13H8V18z" fill="#fff"/><circle cx="18" cy="21" r="5" fill="#1c1c1c"/></svg>REAL ESTATE</div>
  <div class="cta"><svg class="ico" viewBox="0 0 36 36"><rect x="6" y="8" width="16" height="7" rx="1" fill="#fff" transform="rotate(-35 14 12)"/><rect x="15" y="14" width="4" height="18" fill="#fff" transform="rotate(-35 17 23)"/><rect x="4" y="30" width="16" height="3" fill="#fff"/></svg>AUCTIONS</div>
  <div class="cta current"><svg class="ico" viewBox="0 0 36 36"><circle cx="15" cy="15" r="9" fill="none" stroke="#fff" stroke-width="3"/><path d="M22 22l9 9" stroke="#fff" stroke-width="4"/></svg>LIQUIDATIONS</div>
  <div class="cta"><svg class="ico" viewBox="0 0 36 36"><rect x="7" y="5" width="22" height="28" rx="2" fill="none" stroke="#fff" stroke-width="2.5"/><path d="M12 13h12M12 19h12M12 25h8" stroke="#fff" stroke-width="2.5"/></svg>APPRAISALS</div>
</div>

<h2 class="section-title abs" style="left:172px;top:719px">AUCTIONS</h2>

<!-- auction cards -->
<article class="auction abs" style="top:751px">
  <div class="auction-head">AUCTIONS&nbsp; 1</div>
  <div class="thumb abs" role="img" aria-label="Photo of a modern house at dusk" style="background:linear-gradient(#6d86b8,#c7cfdc 60%,#6a7280)"></div>
  <div class="tools abs">
    <div class="tool"><svg viewBox="0 0 13 13"><rect x="1" y="3" width="11" height="8" fill="#444"/></svg>Photos</div>
    <div class="tool"><svg viewBox="0 0 13 13"><rect x="2" y="1" width="9" height="11" fill="#444"/></svg>Videos</div>
    <div class="tool"><svg viewBox="0 0 13 13"><rect x="2" y="1" width="9" height="11" fill="none" stroke="#444"/></svg>Details</div>
  </div>
  <div class="blurb abs"><h3>Lorem Ipsum is simply dummy text of the printing and typesetting industry.</h3><p>Lorem Ipsum has been the industry's standard dummy text ever since the 1500s, when an unknown printer took a galley of type and scrambled it to make a type specimen book.</p></div>
  <div class="details abs"><h4>Live On-Site Auction with Online Bidding</h4>Begins:&nbsp; Thursday, May 24, 2018 at 6:00 AM EDT<br>Ends:&nbsp; Sunday, May 27, 2018 at 6:00 AM EDT<br>Location:P.O. Box 41207, Ashford, VA 24099<br><span class="btn-bid"><svg viewBox="0 0 14 14"><path d="M2 12 9 5M7 2l5 5" stroke="#fff" stroke-width="2.2"/></svg>Click here for Online Bidding</span></div>
</article>

<article class="auction abs" style="top:1136px">
  <div class="auction-head">AUCTIONS&nbsp; 2</div>
  <div class="thumb abs" role="img" aria-label="Photo of a suburban house with a garage" style="background:linear-gradient(#8fb4dc,#d9cdbb 55%,#7a6a58)"></div>
  <div class="tools abs">
    <div class="tool"><svg viewBox="0 0 13 13"><rect x="1" y="3" width="11" height="8" fill="#444"/></svg>Photos</div>
    <div class="tool"><svg viewBox="0 0 13 13"><rect x="2" y="1" width="9" height="11" fill="#444"/></svg>Videos</div>
    <div class="tool"><svg viewBox="0 0 13 13"><rect x="2" y="1" width="9" height="11" fill="none" stroke="#444"/></svg>Details</div>
  </div>
  <div class="blurb abs"><h3>Lorem Ipsum is simply dummy text of the printing and typesetting industry.</h3><p>Lorem Ipsum has been the industry's standard dummy text ever since the 1500s, when an unknown printer took a galley of type and scrambled it to make a type specimen book.</p></div>
  <div class="details abs"><h4>Live On-Site Auction with Online Bidding</h4>Begins:&nbsp; Thursday, May 24, 2018 at 6:00 AM EDT<br>Ends:&nbsp; Sunday, May 27, 2018 at 6:00 AM EDT<br>Location:P.O. Box 41207, Ashford, VA 24099<br><span class="btn-bid"><svg viewBox="0 0 14 14"><path d="M2 12 9 5M7 2l5 5" stroke="#fff" stroke-width="2.2"/></svg>Click here for Online Bidding</span></div>
</article>

<article class="auction abs" style="top:1520px">
  <div class="auction-head">AUCTIONS&nbsp; 3</div>
  <div class="thumb abs" role="img" aria-label="Photo of a family in front of a house" style="background:linear-gradient(#b8c9d8,#8f8a7e 50%,#5f8a3e)"></div>
  <div class="tools abs">
    <div class="tool"><svg viewBox="0 0 13 13"><rect x="1" y="3" width="11" height="8" fill="#444"/></svg>Photos</div>
    <div class="tool"><svg viewBox="0 0 13 13"><rect x="2" y="1" width="9" height="11" fill="#444"/></svg>Videos</div>
    <div class="tool"><svg viewBox="0 0 13 13"><rect x="2" y="1" width="9" height="11" fill="none" stroke="#444"/></svg>Details</div>
  </div>
  <div class="blurb abs"><h3>Lorem Ipsum is simply dummy text of the printing and typesetting industry.</h3><p>Lorem Ipsum has been the industry's standard dummy text ever since the 1500s, when an unknown printer took a galley of type and scrambled it to make a type specimen book.</p></div>
  <div class="details abs"><h4>Live On-Site Auction with Online Bidding</h4>Begins:&nbsp; Thursday, May 24, 2018 at 6:00 AM EDT<br>Ends:&nbsp; Sunday, May 27, 2018 at 6:00 AM EDT<br>Location:P.O. Box 41207, Ashford, VA 24099<br><span class="btn-bid"><svg viewBox="0 0 14 14"><path d="M2 12 9 5M7 2l5 5" stroke="#fff" stroke-width="2.2"/></svg>Click here for Online Bidding</span></div>
</article>

<article class="auction abs" style="top:1903px">
  <div class="auction-head">AUCTIONS&nbsp; 4</div>
  <div class="thumb abs" role="img" aria-label="Photo of a two-storey house" style="background:linear-gradient(#c9d2dc,#8a7865 55%,#5b5248)"></div>
  <div class="tools abs">
    <div class="tool"><svg viewBox="0 0 13 13"><rect x="1" y="3" width="11" height="8" fill="#444"/></svg>Photos</div>
    <div class="tool"><svg viewBox="0 0 13 13"><rect x="2" y="1" width="9" height="11" fill="#444"/></svg>Videos</div>
    <div class="tool"><svg viewBox="0 0 13 13"><rect x="2" y="1" width="9" height="11" fill="none" stroke="#444"/></svg>Details</div>
  </div>
  <div class="blurb abs"><h3>Lorem Ipsum is simply dummy text of the printing and typesetting industry.</h3><p>Lorem Ipsum has been the industry's standard dummy text ever since the 1500s, when an unknown printer took a galley of type and scrambled it to make a type specimen book.</p></div>
  <div class="details abs"><h4>Live On-Site Auction with Online Bidding</h4>Begins:&nbsp; Thursday, May 24, 2018 at 6:00 AM EDT<br>Ends:&nbsp; Sunday, May 27, 2018 at 6:00 AM EDT<br>Location:P.O. Box 41207, Ashford, VA 24099<br><span class="btn-bid"><svg viewBox="0 0 14 14"><path d="M2 12 9 5M7 2l5 5" stroke="#fff" stroke-width="2.2"/></svg>Click here for Online Bidding</span></div>
</article>

<div class="pager abs"><span>‹</span><span>1</span><span>2</span><span>3</span><span class="on">4</span><span>5</span><span class="gap">....</span><span>15</span><span>30</span><span>45</span><span>›</span></div>

<!-- sidebar -->
<aside class="widget abs" style="top:710px;height:393px">
  <div class="widget-title">FEATURED PROPERTY <span class="arrows">‹›</span></div>
  <div class="w-img" role="img" aria-label="Photo of a modern villa with a pool" style="background:linear-gradient(#3c5068,#9ba8b4 55%,#4d7a5a)"></div>
  <p class="w-lead">Lorem Ipsum is simply dummy text of the printing and typesetting industry.</p>
  <p class="w-text">Live On-Site Auction with Online Bidding<br>Begins:&nbsp; Thursday, May 24, 2018 at 6:00 AM EDT<br>Ends:&nbsp; Sunday, May 27, 2018 at 6:00 AM EDT<br>Location:P.O. Box 41207, Ashford, VA 24099</p>
  <span class="btn-small">View Details</span>
</aside>

<aside class="widget abs" style="top:1127px;height:826px">
  <div class="widget-title">NEWS &amp; EVENTS BLOG</div>
  <div class="w-img" role="img" aria-label="Photo of a modern house lit at night" style="height:174px;margin-top:28px;background:linear-gradient(#1f3f78,#6b7d95 55%,#6b5a48)"></div>
  <p class="posted">Posted By 20-7-2014</p>
  <p class="w-lead" style="margin-top:4px">Lorem Ipsum is simply dummy text of the printing and typesetting industry.</p>
  <p class="w-text">Lorem Ipsum has been the industry's standard dummy text ever since the 1500s, when an known printer took a galley of type and scrambled .</p>
  <span class="btn-small">Read More</span>
  <div class="w-img" role="img" aria-label="Photo of a modern house with a lawn" style="height:174px;margin-top:24px;background:linear-gradient(#3d7ac2,#9fb8cf 55%,#4b7a3c)"></div>
  <p class="posted">Posted By 20-7-2014</p>
  <p class="w-lead" style="margin-top:4px">Lorem Ipsum is simply dummy text of the printing and typesetting industry.</p>
  <p class="w-text">Lorem Ipsum has been the industry's standard dummy text ever since the 1500s, when an known printer took a galley of type and scrambled .</p>
  <span class="btn-small">Read More</span>
</aside>

<aside class="widget abs" style="top:1978px;height:340px">
  <div class="widget-title">TESTIMONIALS <span class="arrows">‹›</span></div>
  <div class="quote-person"><div class="avatar" role="img" aria-label="Portrait photo of the client"></div><div><b>Daniel Harrow</b><small>Company Name</small></div></div>
  <div class="qmark">“</div>
  <p class="w-text">Lorem ipsum dolor sit amet, consectetur adipisicing elit, sed do eiusmod tempor incididunt ut labore et dolore magna aliqua. Ut enim ad mainim veniam, quis nostrud exercitation ullamco laboris nisi ut aliquip ex ea commodo consequat.</p>
</aside>

<!-- accreditations -->
<section class="accred abs">
  <span class="accred-label abs">Accreditations</span>
  <div class="badges abs"><span class="badge"></span><span class="badge"></span><span class="badge round"></span><span class="badge"></span><span class="badge"></span><span class="badge round"></span></div>
</section>

<footer class="footer abs">
  <div class="f-col abs" style="left:172px">
    <h5>QUICK LINKS</h5>
    <ul><li>Home</li><li>Auctions</li><li>Services</li><li>Real Estate</li><li>Previous Auctions</li><li>About Us</li><li>Contact Us</li></ul>
  </div>
  <div class="f-col abs" style="left:342px">
    <h5>CONTACT INFO</h5>
    <p>Harrow &amp; Vale Office<br>48 Linden Court<br>20417 Eastbrook<br>Germany<br>Telephone: +49 30 5550 1842<br>E-mail: hello@brevinmail.example</p>
  </div>
  <div class="f-col abs" style="left:570px;width:250px">
    <h5 style="display:flex;justify-content:space-between">NEWS POST <span class="arrows">‹›</span></h5>
    <div class="newsitem"><div class="date">SEP<br>2014</div><div><h6>Lorem ipsum dolor sit amet, consectetur adipisicing elit</h6><p>Sed do eiusmod tempor incididunt ut laobore et dolore magna aliqua. Ut enim ad mainim veniam, quis nostrud exercitation ullamco laboris nisi ut aliquip</p></div></div>
  </div>
  <div class="f-col abs" style="left:899px">
    <h5>CONNECT WITH US</h5>
    <ul class="social"><li>Social Page<i></i></li><li>Microblog<i></i></li><li>Video Channel<i></i></li><li>RSS Feeds<i></i></li></ul>
  </div>
</footer>
<div class="copyright abs">© 2014 Company Name .All Rights Reserved</div>

</body>
</html>
```